Bramble Hollow Networks - Electrical

We need flyers for electrical services.
Areas of work include new builds, office fitouts, switchboard upgrades, installation of ceiling fans, powerpoint and downlight upgrades, home theatre and AV systems, all exterior and emergency work. Free quotes
We would like to see designs with the colour Red with a young and modern design. Licence No: 63914K must be included and call Leopold on 0438917062.

Colors
ec1f27

```html
<!DOCTYPE html>
<html lang="en">
<head>
<meta charset="utf-8">
<title>Bramble Hollow Networks – Electrical Services Flyer</title>
<link rel="stylesheet" href="https://fonts.googleapis.com/css2?family=Exo+2:wght@600;700&family=Source+Sans+3:wght@600;700&family=Cinzel:wght@400;500&family=Open+Sans:wght@400;700&display=swap">
<style>
  :root {
    --brand-red: #ec1f27;
    --brand-red-dark: #b5141a;
    --ink: #111111;
    --panel-grey: #c4c4c4;
    --pill-grey: #c9c9c9;
    --white: #ffffff;
  }
  * { box-sizing: border-box; margin: 0; padding: 0; }
  html, body { width: 920px; height: 1200px; overflow: hidden; background: #2a2a2b; }
  .flyer { position: relative; width: 920px; height: 1200px; background: var(--ink); font-family: "Source Sans 3", sans-serif; }

  .masthead {
    position: absolute; left: 0; top: 0; width: 920px; height: 198px;
    background: linear-gradient(180deg, var(--brand-red) 0%, #d81a21 70%, var(--brand-red-dark) 100%);
    color: var(--white); text-align: center; font-family: "Exo 2", sans-serif;
  }
  .masthead .company { position: absolute; top: 48px; width: 100%; font-size: 33px; font-weight: 600; letter-spacing: 0.5px; }
  .masthead .service { position: absolute; top: 92px; width: 100%; font-size: 68px; font-weight: 700; letter-spacing: 1px; }

  .feature { position: absolute; left: 0; top: 208px; width: 920px; height: 495px; background: var(--panel-grey); overflow: hidden; }
  .feature-photo {
    position: absolute; left: 0; top: 0; width: 600px; height: 495px;
    background: linear-gradient(100deg, #b89a88 0%, #d9d5d0 30%, #a9a9a6 55%, rgba(196,196,196,0) 100%);
  }
  .contact-tab {
    position: absolute; left: 0; top: 0; height: 50px; width: 420px;
    background: var(--ink); clip-path: polygon(0 0, 100% 0, 93% 100%, 0 100%);
    color: var(--white); font-weight: 700; font-size: 32px; padding: 4px 0 0 53px; letter-spacing: 0.3px;
  }
  .work-title {
    position: absolute; left: 495px; top: 44px; font-family: "Exo 2", sans-serif;
    font-size: 35px; font-weight: 600; color: var(--ink);
  }
  .work-title-rule { position: absolute; left: 495px; top: 90px; }
  .work-list { position: absolute; left: 550px; top: 128px; list-style: none; width: 360px; }
  .work-list li { position: relative; padding-left: 42px; font-size: 25px; font-weight: 600; line-height: 31px; color: var(--ink); margin-bottom: 9px; }
  .work-list li svg { position: absolute; left: 0; top: 6px; }

  .divider { position: absolute; left: 0; top: 703px; width: 920px; height: 8px; background: var(--brand-red); }

  .showcase { position: absolute; left: 0; top: 711px; width: 920px; height: 430px; background: radial-gradient(ellipse at center, #1d1d1d 0%, #0b0b0b 100%); }
  .showcase-headline { position: absolute; top: 20px; width: 100%; text-align: center; color: var(--white); font-weight: 700; font-size: 31px; }
  .gallery { position: absolute; top: 81px; left: 44px; display: flex; gap: 8px; }
  .gallery-tile { width: 272px; height: 185px; border-radius: 8px; }
  .tile-fan { background: linear-gradient(135deg, #8a6a4a 0%, #d8d2c8 45%, #7fa2c6 100%); }
  .tile-cables { background: linear-gradient(135deg, #f3f3f3 0%, #e6d36a 40%, #4b8a3b 65%, #e2e2e2 100%); }
  .tile-panel { background: linear-gradient(135deg, #d4a38f 0%, #c9d3db 45%, #3e6fb0 70%, #9fa9ae 100%); }

  .perks {
    position: absolute; left: 110px; top: 293px; width: 698px; height: 41px; border-radius: 21px;
    background: var(--pill-grey); display: flex; align-items: center; justify-content: center; gap: 18px;
    font-size: 21px; font-weight: 700; color: #2b2b2b;
  }
  .perks span { display: flex; align-items: center; gap: 6px; }
  .perks .light { font-weight: 600; }

  .call-line { position: absolute; top: 335px; width: 100%; text-align: center; color: var(--white); font-family: "Cinzel", serif; font-size: 40px; letter-spacing: 1px; }
  .call-line .number { font-size: 52px; font-weight: 500; }

  .footer-band {
    position: absolute; left: 0; top: 1141px; width: 920px; height: 59px; background: var(--brand-red);
    color: var(--white); font-family: "Open Sans", sans-serif;
  }
  .licence { position: absolute; left: 37px; top: 15px; font-size: 20px; letter-spacing: 1.5px; }
  .email { position: absolute; right: 36px; top: 9px; font-size: 27px; font-weight: 700; letter-spacing: 1.5px; }
</style>
</head>
<body>
<svg width="0" height="0" style="position:absolute">
  <symbol id="tick-badge" viewBox="0 0 24 24">
    <circle cx="12" cy="12" r="11" fill="#ec1f27"/>
    <path d="M6.5 12.5l3.8 3.8 7.5-8.5" fill="none" stroke="#fff" stroke-width="2.6" stroke-linecap="round" stroke-linejoin="round"/>
  </symbol>
</svg>

<main class="flyer">
  <header class="masthead">
    <div class="company">BRAMBLE HOLLOW NETWORKS</div>
    <h1 class="service">ELECTRICAL SERVICES</h1>
  </header>

  <section class="feature">
    <div class="feature-photo" role="img" aria-label="Electrician's hands wiring an open junction box on a wall"></div>
    <div class="contact-tab">Contact Us Today</div>
    <h2 class="work-title">Areas of Work Include</h2>
    <svg class="work-title-rule" width="355" height="8" viewBox="0 0 355 8"><path d="M2 5 Q120 1 353 4" stroke="#111" stroke-width="4" fill="none" stroke-linecap="round"/></svg>
    <ul class="work-list">
      <li><svg width="24" height="24"><use href="#tick-badge"/></svg>New builds</li>
      <li><svg width="24" height="24"><use href="#tick-badge"/></svg>Office Fitouts</li>
      <li><svg width="24" height="24"><use href="#tick-badge"/></svg>Switchboard upgrades</li>
      <li><svg width="24" height="24"><use href="#tick-badge"/></svg>Installation of ceiling fans</li>
      <li><svg width="24" height="24"><use href="#tick-badge"/></svg>Powerpoint and<br>downlight upgrades</li>
      <li><svg width="24" height="24"><use href="#tick-badge"/></svg>Home theatre and AV<br>systems</li>
      <li><svg width="24" height="24"><use href="#tick-badge"/></svg>All exterior and<br>emergency work</li>
    </ul>
  </section>

  <div class="divider"></div>

  <section class="showcase">
    <p class="showcase-headline">Lorem ipsum dolor sit amet, consectetur adipiscing</p>
    <div class="gallery">
      <div class="gallery-tile tile-fan" role="img" aria-label="Electrician fitting a ceiling fan"></div>
      <div class="gallery-tile tile-cables" role="img" aria-label="Coloured cables on a wiring plan"></div>
      <div class="gallery-tile tile-panel" role="img" aria-label="Testing a switchboard with a multimeter"></div>
    </div>
    <div class="perks">
      <span><svg width="20" height="20"><use href="#tick-badge"/></svg>FREE QUOTES AVAILABLE</span>
      <span><svg width="20" height="20"><use href="#tick-badge"/></svg>GUARANTEED</span>
      <span class="light"><svg width="20" height="20"><use href="#tick-badge"/></svg>SATISFACTION</span>
    </div>
    <p class="call-line">CALL LEOPOLD ON : <span class="number">0438917062</span></p>
  </section>

  <footer class="footer-band">
    <span class="licence">Licence No: 63914K</span>
    <span class="email">info@bramblehollownet.com</span>
  </footer>
</main>
</body>
</html>
```